Letterhead Design Project

Professional but modern letterhead.

Target Market(s)

mining companies

Industry/Entity Type

It Professional

Colors

Designer to choose colors to be used in the design.

```html
<!DOCTYPE html>
<html lang="en">
<head>
<meta charset="utf-8">
<title>Oreline Letterhead</title>
<link rel="stylesheet" href="https://fonts.googleapis.com/css2?family=Carlito:wght@400;700&display=swap">
<style>
  :root {
    --brand-blue: #0531da;
    --band-black: #1d1d1d;
    --paper: #ffffff;
    --ink: #111111;
    --ghost: #f1f1f1;
  }
  html, body {
    margin: 0;
    padding: 0;
    overflow: hidden;
    background: var(--paper);
  }
  .letterhead {
    position: relative;
    width: 849px;
    height: 1200px;
    overflow: hidden;
    background: var(--paper);
    font-family: "Carlito", "Calibri", sans-serif;
    color: var(--ink);
  }
  .brand-header {
    position: absolute;
    top: 40px;
    left: 0;
    width: 849px;
    text-align: center;
  }
  .brand-dot {
    display: block;
    width: 90px;
    height: 90px;
    margin: 0 auto 36px;
    border-radius: 50%;
    background: var(--brand-blue);
  }
  .brand-name {
    margin: 0;
    font-size: 58px;
    font-weight: 700;
    letter-spacing: 2px;
    color: var(--brand-blue);
    line-height: 1;
  }
  .ghost-name {
    position: absolute;
    left: 30px;
    top: 860px;
    margin: 0;
    font-size: 118px;
    font-weight: 700;
    color: var(--ghost);
    line-height: 1;
    letter-spacing: 2px;
  }
  .footer-wave {
    position: absolute;
    left: 0;
    top: 0;
  }
  .contact-list {
    position: absolute;
    left: 42px;
    top: 951px;
    margin: 0;
    padding: 0;
    list-style: none;
    font-size: 19.5px;
    line-height: 26px;
  }
  .contact-item {
    display: flex;
    align-items: flex-start;
    margin-bottom: 3px;
  }
  .contact-icon {
    flex: none;
    width: 20px;
    height: 20px;
    margin: 3px 10px 0 0;
  }
  .corner-name {
    position: absolute;
    right: 26px;
    top: 1108px;
    margin: 0;
    font-size: 28px;
    font-weight: 700;
    color: var(--paper);
    letter-spacing: 1px;
  }
</style>
</head>
<body>
<main class="letterhead">
  <p class="ghost-name">ORELINE</p>

  <header class="brand-header">
    <span class="brand-dot"></span>
    <h1 class="brand-name">ORELINE</h1>
  </header>

  <svg class="footer-wave" width="849" height="1200" viewBox="0 0 849 1200" aria-hidden="true">
    <path d="M0 1158 Q 520 1165 849 1004 L849 1200 L0 1200 Z" fill="var(--band-black)"/>
    <path d="M0 1172 Q 545 1172 849 1026 L849 1200 L0 1200 Z" fill="var(--brand-blue)"/>
  </svg>

  <ul class="contact-list">
    <li class="contact-item">
      <svg class="contact-icon" viewBox="0 0 20 20" aria-hidden="true">
        <circle cx="10" cy="10" r="10" fill="var(--brand-blue)"/>
        <path d="M4.5 10.5 L10 5.5 L15.5 10.5 M6.5 9.5 V14.5 H13.5 V9.5" fill="none" stroke="#fff" stroke-width="1.6" stroke-linejoin="round"/>
      </svg>
      <span>Suite # 410, Vale Bldg<br>NY 10482</span>
    </li>
    <li class="contact-item">
      <svg class="contact-icon" viewBox="0 0 20 20" aria-hidden="true">
        <circle cx="10" cy="10" r="10" fill="var(--brand-blue)"/>
        <path d="M6 13.5 C8 11 11 8 13.8 6 L15 7.5 C12.5 9.5 9.5 12.5 7.5 15 Z" fill="#fff"/>
      </svg>
      <span>212-555-0147</span>
    </li>
    <li class="contact-item">
      <svg class="contact-icon" viewBox="0 0 20 20" aria-hidden="true">
        <circle cx="10" cy="10" r="10" fill="var(--brand-blue)"/>
        <rect x="5.5" y="8" width="9" height="7" fill="#fff"/>
        <rect x="7.5" y="5" width="5" height="3.5" fill="#fff"/>
        <rect x="7.5" y="10" width="5" height="1.2" fill="var(--brand-blue)"/>
      </svg>
      <span>212-555-0193</span>
    </li>
    <li class="contact-item">
      <svg class="contact-icon" viewBox="0 0 20 20" aria-hidden="true">
        <circle cx="10" cy="10" r="10" fill="var(--brand-blue)"/>
        <rect x="4.5" y="6.5" width="11" height="7.5" fill="#fff"/>
        <path d="M4.5 6.5 L10 11 L15.5 6.5" fill="none" stroke="var(--brand-blue)" stroke-width="1"/>
      </svg>
      <span>hello@oreline.com</span>
    </li>
    <li class="contact-item">
      <svg class="contact-icon" viewBox="0 0 20 20" aria-hidden="true">
        <circle cx="10" cy="10" r="10" fill="var(--brand-blue)"/>
        <g fill="none" stroke="#fff" stroke-width="1.2">
          <circle cx="10" cy="10" r="5.5"/>
          <ellipse cx="10" cy="10" rx="2.4" ry="5.5"/>
          <path d="M4.5 10 H15.5 M5.5 7.3 H14.5 M5.5 12.7 H14.5"/>
        </g>
      </svg>
      <span>www.oreline.com</span>
    </li>
  </ul>

  <p class="corner-name">ORELINE</p>
</main>
</body>
</html>
```